High End Business Card Design for Flooring Store

Looking for a new card design for our hardwood flooring company. We have no print budget for these and are open to cards made from wood, metal, cardstock with embossed print ... or any combination of these. No plastic.

We sell luxury products and I want the cards to reflect our image of quality and class.

Our contact information as such;
Employee Name
418 Colbrook Blvd.
Ashwick, NS
K9R-3M5
(555) 214-3968
Employee email @velkaflooring.com

Target Market(s)

Home Builders

Contact Information for Business Card

Emnployee name, business contact information

```html
<!DOCTYPE html>
<html lang="en">
<head>
<meta charset="utf-8">
<title>Velka Flooring — Business Card</title>
<link href="https://fonts.googleapis.com/css2?family=Montserrat:wght@400;500;700&display=swap" rel="stylesheet">
<style>
  :root {
    --stage: #2a2a2a;
    --card-red: #9a2620;
    --card-red-deep: #8a211c;
    --card-dark: #161616;
    --card-dark-soft: #1d1d1d;
    --brand-red: #a22a22;
    --gold: #e8b22a;
    --white: #ffffff;
    --muted: #7a7a7a;
  }
  * { box-sizing: border-box; margin: 0; padding: 0; }
  html, body {
    width: 1200px; height: 1200px; overflow: hidden;
    background: var(--stage);
    font-family: "Montserrat", sans-serif;
  }
  .canvas { position: relative; width: 1200px; height: 1200px; }

  .card {
    position: absolute;
    border-radius: 22px;
    overflow: hidden;
    box-shadow: 0 18px 40px rgba(0,0,0,.45);
  }

  /* Front */
  .card-front {
    left: 80px; top: 300px; width: 600px; height: 343px;
    background: linear-gradient(160deg, var(--card-red), var(--card-red-deep));
    display: flex; align-items: center; justify-content: center;
  }
  .card-front .texture {
    position: absolute; inset: 0;
    background: linear-gradient(135deg, rgba(255,255,255,.03), rgba(0,0,0,.05));
  }
  .front-wordmark {
    position: relative;
    display: flex; align-items: center; gap: 14px;
  }
  .front-wordmark .mark-square {
    width: 34px; height: 34px; background: var(--gold);
  }
  .front-wordmark .name {
    color: var(--white);
    font-weight: 500;
    font-size: 78px;
    letter-spacing: 1px;
    line-height: 1;
  }

  /* Back */
  .card-back {
    left: 760px; top: 186px; width: 343px; height: 600px;
    background: linear-gradient(200deg, var(--card-dark-soft), var(--card-dark) 60%);
    padding: 48px 36px 44px;
    display: flex; flex-direction: column;
  }
  .back-brand { text-align: right; }
  .back-brand .brand-row {
    display: flex; align-items: center; justify-content: flex-end; gap: 10px;
  }
  .back-brand .mark-square { width: 22px; height: 22px; background: var(--gold); }
  .back-brand .name {
    color: var(--brand-red); font-weight: 500; font-size: 62px; line-height: 1;
  }
  .back-brand .tagline {
    margin-top: 8px;
    color: var(--muted); font-size: 15px; line-height: 1.35;
  }

  .employee {
    margin-top: 70px;
    text-align: center;
  }
  .employee .employee-name {
    color: var(--brand-red); font-weight: 700; font-size: 24px; letter-spacing: .5px;
  }
  .employee .rule {
    width: 110px; height: 1px; background: var(--gold); margin: 16px auto 0;
  }

  .contact {
    margin-top: auto;
    list-style: none;
    display: flex; flex-direction: column; gap: 16px;
  }
  .contact li {
    display: flex; align-items: flex-start; gap: 14px;
    color: var(--muted); font-size: 15px; line-height: 1.4;
  }
  .contact svg { flex: 0 0 16px; width: 16px; height: 16px; margin-top: 2px; }
</style>
</head>
<body>
<main class="canvas">

  <section class="card card-front" aria-label="Card front">
    <div class="texture" role="img" aria-label="Subtle embossed tone-on-tone pattern"></div>
    <div class="front-wordmark">
      <span class="mark-square"></span>
      <span class="name">Velka</span>
    </div>
  </section>

  <section class="card card-back" aria-label="Card back">
    <header class="back-brand">
      <div class="brand-row">
        <span class="mark-square"></span>
        <span class="name">Velka</span>
      </div>
      <p class="tagline">Planchers &amp; Escaliers<br>Flooring &amp; Stairs</p>
    </header>

    <div class="employee">
      <p class="employee-name">Employee Name</p>
      <div class="rule"></div>
    </div>

    <ul class="contact">
      <li>
        <svg viewBox="0 0 16 16" aria-hidden="true"><path fill="var(--gold)" d="M8 0a5.5 5.5 0 0 0-5.5 5.5C2.5 9.6 8 16 8 16s5.5-6.4 5.5-10.5A5.5 5.5 0 0 0 8 0zm0 7.8a2.3 2.3 0 1 1 0-4.6 2.3 2.3 0 0 1 0 4.6z"/></svg>
        <span>418 Colbrook Blvd.<br>Ashwick, NS K9R-3M5</span>
      </li>
      <li>
        <svg viewBox="0 0 16 16" aria-hidden="true"><path fill="var(--gold)" d="M3.6 1l2.3 2.9-1.4 1.8a9.5 9.5 0 0 0 5.8 5.8l1.8-1.4L15 12.4 13.4 15C6.6 14.6 1.4 9.4 1 2.6L3.6 1z"/></svg>
        <span>(555) 214-3968</span>
      </li>
      <li>
        <svg viewBox="0 0 16 16" aria-hidden="true"><path fill="var(--gold)" d="M1 3h14v10H1V3zm1.5 1.3v.3L8 8.7l5.5-4.1v-.3h-11z"/></svg>
        <span>email@velkaflooring.com</span>
      </li>
    </ul>
  </section>

</main>
</body>
</html>
```